Stationary and Business Card Design

We need a stationery design and a business card design for a non-profit economics development agency. Our website is brightledgerhub.org. Our clients are Canadian government agencies and large Chinese company. We need the design to be professional and corporate.

Please see attached for our Power Point presentation. Please take design elements from our website and our ppt.

```html
<!DOCTYPE html>
<html lang="en">
<head>
<meta charset="utf-8">
<title>Bright Ledger Alliance – Business Card</title>
<link href="https://fonts.googleapis.com/css2?family=Open+Sans:wght@400;600;700&display=swap" rel="stylesheet">
<style>
  :root {
    --page-bg: #e9e7e4;
    --card-white: #f4f4f4;
    --card-dark: #333234;
    --brand-red: #e31b2a;
    --text-light: #d9d9d9;
    --text-white: #ffffff;
  }
  * { margin: 0; padding: 0; box-sizing: border-box; }
  html, body {
    width: 1200px;
    height: 900px;
    overflow: hidden;
    background: var(--page-bg);
    font-family: "Open Sans", Arial, sans-serif;
  }
  .stage {
    width: 1200px;
    height: 900px;
    display: flex;
    flex-direction: column;
    align-items: center;
    justify-content: center;
    gap: 60px;
  }
  .card {
    width: 600px;
    height: 343px;
    background: var(--card-white);
    box-shadow: 0 6px 18px rgba(0,0,0,0.15);
    position: relative;
    overflow: hidden;
  }
  .brand {
    display: flex;
    align-items: center;
    gap: 10px;
    color: var(--brand-red);
    font-weight: 700;
    font-size: 26px;
    line-height: 1.2;
    white-space: nowrap;
  }
  .brand-square {
    width: 18px;
    height: 18px;
    flex: none;
    background: var(--brand-red);
  }
  .card-front {
    display: flex;
    align-items: center;
    justify-content: center;
  }
  .card-back { display: flex; }
  .contact-panel {
    width: 46%;
    height: 100%;
    background: var(--card-dark);
    color: var(--text-light);
    padding: 44px 24px 0 34px;
    font-size: 12.5px;
    line-height: 1.55;
  }
  .person-name {
    color: var(--text-white);
    font-weight: 700;
    font-size: 16px;
  }
  .person-role { margin-bottom: 18px; }
  .address { margin-bottom: 10px; }
  .contact-list { list-style: none; }
  .contact-list li {
    display: flex;
    align-items: center;
    gap: 10px;
  }
  .contact-icon {
    width: 11px;
    height: 11px;
    flex: none;
  }
  .brand-panel {
    width: 54%;
    height: 100%;
    position: relative;
    display: flex;
    justify-content: center;
    align-items: flex-start;
    padding-top: 78px;
  }
  .brand-panel .brand { font-size: 22px; }
  .red-band {
    position: absolute;
    left: 0;
    right: 0;
    bottom: 0;
    height: 16px;
    background: var(--brand-red);
  }
</style>
</head>
<body>
<main class="stage">
  <section class="card card-front" aria-label="Business card front">
    <div class="brand">
      <span class="brand-square"></span>
      <span class="brand-name">Bright Ledger Alliance</span>
    </div>
  </section>

  <section class="card card-back" aria-label="Business card back">
    <div class="contact-panel">
      <p class="person-name">Alan Mercer</p>
      <p class="person-role">President</p>
      <p class="address">Bright Ledger Alliance<br>Harbour Lane 4 // 10482 canada</p>
      <ul class="contact-list">
        <li>
          <svg class="contact-icon" viewBox="0 0 12 12" aria-hidden="true"><path d="M2.5 1 L4.5 1 L5.2 3.6 L4 4.6 Q5 7 7.4 8 L8.4 6.8 L11 7.5 L11 9.5 Q10.5 11 9 11 Q1 10 1 3 Q1 1.5 2.5 1 Z" fill="var(--brand-red)"/></svg>
          +49 (0) 40 55501234
        </li>
        <li>
          <svg class="contact-icon" viewBox="0 0 12 12" aria-hidden="true"><rect x="3" y="0.5" width="6" height="11" rx="1.2" fill="var(--brand-red)"/><rect x="4" y="2" width="4" height="7" fill="var(--card-dark)"/></svg>
          +49 (0) 151 55507788
        </li>
        <li>
          <svg class="contact-icon" viewBox="0 0 12 12" aria-hidden="true"><rect x="0.5" y="2" width="11" height="8" fill="var(--brand-red)"/><path d="M0.5 2 L6 6.5 L11.5 2" stroke="var(--card-dark)" stroke-width="1" fill="none"/></svg>
          alan@brightledgerhub.org
        </li>
        <li>
          <svg class="contact-icon" viewBox="0 0 12 12" aria-hidden="true"><circle cx="6" cy="6" r="5" fill="none" stroke="var(--brand-red)" stroke-width="1.2"/><path d="M1 6 H11 M6 1 Q3 6 6 11 Q9 6 6 1" stroke="var(--brand-red)" stroke-width="1" fill="none"/></svg>
          www.brightledgerhub.org
        </li>
      </ul>
    </div>
    <div class="brand-panel">
      <div class="brand">
        <span class="brand-square"></span>
        <span class="brand-name">Bright Ledger Alliance</span>
      </div>
      <div class="red-band"></div>
    </div>
  </section>
</main>
</body>
</html>
```